Financial Statements templates

We are a accounting and bookkeeping firms, we are trying to change the presentation of the clients' financial statements in a more professional and interesting way using graphics and PowerPoint skills, each client should feel that his/her FS are unique and developed for him/her, first will start with the normal financial statements (Balance sheet, income statement and cash flow) and then with the financial highlights, ratios and facts where we can use the charts and graphics

Reason: More time for more ideas

Reason: I want to give more time to the participants and i did not quite liked the submitted designs so far

Target Market(s)

different industry

Industry/Entity Type

Accounting

Colors

Requirements
Must have
• We would like to have a template where we can use with different clients as we need to only update their figures and upload their logos along with our below logo i.e. kelvanoro+ as a maker/prepared by. each client should feel that their Financial Statement is customized for them.
• Should also include charts and graphics,

```html
<!DOCTYPE html>
<html lang="en">
<head>
<meta charset="utf-8">
<title>Individual Slides 01A – Financial Statements Template</title>
<link href="https://fonts.googleapis.com/css2?family=Oswald:wght@500&family=Open+Sans:wght@400;600;700;800&display=swap" rel="stylesheet">
<style>
  :root{
    --page:#ffffff;
    --stage:#ece9e4;
    --heading:#b5b0b0;
    --navy:#1f2d45;
    --ink:#1b2a44;
    --blue:#2e6cb0;
    --bright:#1f6fc7;
    --lime:#b9d84a;
    --green:#17a64a;
    --col-blue:#3f6fc4;
    --col-grey:#a9b4c6;
    --red:#c8121b;
    --deep:#1c3a63;
    --orange:#ee7a2b;
    --silver:#9a9a9a;
    --yellow:#f3b712;
    --muted:#7a8290;
  }
  *{box-sizing:border-box;margin:0;padding:0}
  html,body{width:1200px;height:1200px;overflow:hidden;background:var(--page);font-family:"Open Sans",Arial,sans-serif}
  .sheet{position:relative;width:1200px;height:1200px}
  .sheet-title{position:absolute;top:26px;left:0;width:1200px;text-align:center;font-family:"Oswald",Arial,sans-serif;font-weight:500;font-size:52px;letter-spacing:1px;color:var(--heading)}
  .stage{position:absolute;left:146px;width:895px;height:503px;background:var(--stage)}
  .stage.top{top:126px}
  .stage.bottom{top:665px}

  .slide{position:absolute;width:238px;height:134px;background:#fff;overflow:hidden;box-shadow:0 2px 4px rgba(0,0,0,.3)}
  .c1{left:199px}.c2{left:478px}.c3{left:758px}
  .r1{top:150px}.r2{top:303px}.r3{top:461px}
  .r4{top:689px}.r5{top:842px}.r6{top:1000px}

  .brand{position:absolute;display:flex;align-items:center;gap:2px;color:var(--bright);font-weight:800;text-transform:uppercase;letter-spacing:.2px;white-space:nowrap}
  .brand i{display:block;border-radius:50%;background:var(--bright)}
  .brand.sm{font-size:5px}.brand.sm i{width:7px;height:7px}
  .brand.lg{font-size:9px}.brand.lg i{width:16px;height:16px}
  .brand-box{position:absolute;top:2px;left:2px;width:46px;height:22px;background:#fff}

  .maker{position:absolute;color:var(--ink);font-weight:600;white-space:nowrap}
  .prepared{position:absolute;font-size:3px;color:var(--ink)}

  .cover-photo{position:absolute;left:0;top:0;width:238px;height:104px;background:linear-gradient(120deg,#2a3c5c,#1d2b45 55%,#263652)}
  .cover-blue{position:absolute;left:0;top:0;width:238px;height:110px;background:linear-gradient(135deg,#eceef1 0 18%,#1f6fc7 18%,#2272c6 70%,#1c62b0)}
  .band{position:absolute;left:0;width:238px;background:var(--navy)}
  .title{position:absolute;color:#fff;font-weight:700;text-align:center;width:100%}
  .sub{position:absolute;color:var(--lime);font-weight:600;font-size:5px;text-align:center;width:100%}
  .date{position:absolute;color:#fff;font-size:3px;font-style:italic;font-weight:700}
  .tiny{position:absolute;font-size:2.6px;color:#8b93a3}
  .ep{position:absolute;left:4px;font-size:5.5px;font-weight:700;color:var(--ink);line-height:1.25}

  .foot{position:absolute;left:0;bottom:0;width:238px;height:12px;background:#fff}
  .foot .maker{left:9px;top:2px;font-size:5.5px}
  .foot .by{position:absolute;left:4px;top:5px;font-size:2.5px;color:var(--ink)}
  .foot .btn{position:absolute;right:6px;top:4px;width:12px;height:4px;background:var(--deep)}

  .agenda-word{position:absolute;left:10px;top:67px;color:#fff;font-weight:800;font-size:15px}
  .agenda-note{position:absolute;left:10px;top:87px;width:78px;font-size:2.6px;color:#b8c0cc;line-height:1.3}
  .divider{position:absolute;left:101px;top:62px;width:1px;height:28px;background:#6e7a8e}
  .topic{position:absolute;width:50px;text-align:center;color:#fff}
  .topic b{display:block;margin:0 auto 4px;width:21px;height:21px}
  .topic strong{display:block;font-size:6.2px;font-weight:700}
  .topic small{display:block;font-size:4.5px;color:#cfd5de}
  .qa{position:absolute;top:98px;width:20px;text-align:center;font-size:4.6px;color:#fff}

  .head{position:absolute;left:0;top:0;width:238px;height:22px;background:#fff}
  .head h3{position:absolute;left:9px;top:7px;font-size:7.3px;font-weight:700;color:var(--bright);text-transform:uppercase;letter-spacing:.2px}
  .head::before{content:"";position:absolute;left:3px;top:7px;width:2px;height:9px;background:var(--bright)}
  .head small{position:absolute;left:9px;top:16px;font-size:2.6px;color:#8b93a3}
  .head .brand{right:6px;top:8px}
  .chart-area{position:absolute;left:0;top:22px;width:238px;height:100px;background:var(--blue)}
  .chart-area svg{position:absolute;left:4px;top:6px}
  .quarter{position:absolute;right:9px;top:4px;font-size:5px;color:#e6ecf5}
  .val-col{position:absolute;left:164px;top:13px;width:30px;height:87px;background:var(--red)}
  .pct-col{position:absolute;left:194px;top:13px;width:36px;height:87px;background:var(--deep)}
  .val-col em,.pct-col em{display:block;text-align:center;font-style:normal;font-size:3.6px;color:#fff;padding-top:2px}
  .row{position:absolute;left:0;width:230px;height:12px}
  .row .d{position:absolute;right:70px;top:4px;font-size:3.8px;color:#e4ebf5}
  .row .v{position:absolute;left:164px;width:30px;text-align:center;font-size:8.4px;color:#fff}
  .row .p{position:absolute;left:194px;width:36px;text-align:center;font-size:7.4px;color:#fff}

  .block{position:absolute;width:55px}
  .block.b1{left:68px;background:var(--col-blue)}
  .block.b2{left:125px;background:var(--green)}
  .block.b3{left:182px;background:var(--col-grey)}
  .colhead{position:absolute;font-size:2.8px;color:#444}
  .label{position:absolute;left:14px;font-size:2.8px;color:#333}
  .label.sec{left:9px;font-size:3.2px;color:#222}
  .cell{position:absolute;font-size:3px;color:#fff}
  .navband{position:absolute;left:0;width:238px;height:6px;background:var(--navy)}
  .navband span{position:absolute;top:1px;font-size:3px;color:#fff}
  .totals{position:absolute;left:0;width:238px;height:6px}
  .totals span{position:absolute;font-size:3.2px;color:#222}
</style>
</head>
<body>
<div class="sheet">
  <div class="sheet-title">INDIVIDUAL SLIDES - 01A</div>
  <div class="stage top"></div>
  <div class="stage bottom"></div>

  <section class="slide c1 r1">
    <div class="cover-photo" role="img" aria-label="Dark blue photo of a business desk with documents"></div>
    <div class="brand-box"></div>
    <div class="brand sm" style="left:5px;top:10px"><i></i>Velmora</div>
    <div class="title" style="top:44px;font-size:12px">ABC COMPANY</div>
    <div class="sub" style="top:62px">FINANCIAL STATEMENTS</div>
    <div class="date" style="left:200px;top:98px">June 30, 2017</div>
    <div class="tiny" style="left:110px;top:100px">Confidential</div>
    <div class="prepared" style="left:154px;top:109px">Prepared by</div>
    <div class="maker" style="left:154px;top:113px;font-size:11px">kelvanoro+</div>
  </section>

  <section class="slide c2 r1">
    <div class="cover-photo" role="img" aria-label="Dark blue photo of a business desk with documents"></div>
    <div class="brand-box"></div>
    <div class="brand sm" style="left:5px;top:10px"><i></i>Velmora</div>
    <div class="title" style="top:44px;font-size:12px">ABC COMPANY</div>
    <div class="sub" style="top:62px">FINANCIAL STATEMENTS</div>
    <div class="date" style="left:200px;top:98px">June 30, 2017</div>
    <div class="tiny" style="left:110px;top:100px">Confidential</div>
    <div class="ep" style="top:110px">H1 2017<br>Earnings Presentation</div>
    <div class="prepared" style="left:154px;top:109px">Prepared by</div>
    <div class="maker" style="left:154px;top:113px;font-size:11px">kelvanoro+</div>
  </section>

  <section class="slide c3 r1">
    <div class="cover-blue"></div>
    <div class="brand sm" style="left:100px;top:10px"><i></i>Velmora</div>
    <div class="title" style="top:47px;font-size:12px">ABC COMPANY</div>
    <div class="sub" style="top:66px">FINANCIAL STATEMENTS</div>
    <div class="ep" style="top:113px">H1 2017<br>Earnings Presentation</div>
    <div class="prepared" style="left:154px;top:112px">Prepared by</div>
    <div class="maker" style="left:154px;top:116px;font-size:11px">kelvanoro+</div>
  </section>

  <section class="slide c1 r2">
    <div class="brand lg" style="left:80px;top:14px"><i></i>Velmora</div>
    <div class="band" style="top:44px;height:61px"></div>
    <div class="title" style="top:60px;font-size:12px">ABC COMPANY</div>
    <div class="sub" style="top:80px">FINANCIAL STATEMENTS</div>
    <div class="date" style="left:200px;top:99px">June 30, 2017</div>
    <div class="prepared" style="left:154px;top:110px">Prepared by</div>
    <div class="maker" style="left:154px;top:114px;font-size:11px">kelvanoro+</div>
  </section>

  <section class="slide c2 r2">
    <div class="brand lg" style="left:80px;top:14px"><i></i>Velmora</div>
    <div class="band" style="top:44px;height:61px"></div>
    <div class="title" style="top:53px;left:40px;width:auto;font-size:12px;text-align:left;line-height:1.5">H1 2017<br>Earnings Presentation</div>
    <div class="date" style="left:148px;top:90px;font-size:6px">June 30, 2017</div>
    <div class="ep" style="top:113px;font-size:5px">FINANCIAL STATEMENTS</div>
    <div class="tiny" style="left:32px;top:122px">Confidential</div>
    <div class="prepared" style="left:154px;top:110px">Prepared by</div>
    <div class="maker" style="left:154px;top:114px;font-size:11px">kelvanoro+</div>
  </section>

  <section class="slide c3 r2">
    <div class="brand sm" style="left:206px;top:7px"><i></i>Velmora</div>
    <div role="img" aria-label="Portrait photo of the chief executive officer" style="position:absolute;left:98px;top:15px;width:42px;height:42px;border-radius:50%;background:radial-gradient(circle,#c7ccd3,#8e97a5);border:2px solid #e6e8ec"></div>
    <div class="tiny" style="left:0;width:238px;text-align:center;top:64px;color:#666">Chief Executive Officer</div>
    <div style="position:absolute;left:0;width:238px;top:72px;text-align:center;font-size:4.6px;color:var(--bright);font-weight:600">Welcome Introduction</div>
    <div style="position:absolute;left:30px;top:82px;width:178px;font-size:2.6px;line-height:1.6;color:#8b93a3;text-align:center">We are pleased to share the half year results with you. This report sets out the balance sheet, income statement and cash flow along with the main highlights of the period.</div>
    <div class="foot"><div class="by">by</div><div class="maker">kelvanoro+</div><div class="btn"></div></div>
  </section>

  <section class="slide c1 r3">
    <div class="brand lg" style="left:82px;top:14px"><i></i>Velmora</div>
    <div class="band" style="top:53px;height:56px;background:#353f52"></div>
    <div class="agenda-word">AGENDA</div>
    <div class="agenda-note">A short outline of the topics in this half year review.</div>
    <div class="divider"></div>
    <div class="topic" style="left:86px;top:52px"><b style="background:var(--orange)"></b><strong>H1 2017</strong><small>Highlights</small></div>
    <div class="topic" style="left:136px;top:52px"><b style="background:var(--silver)"></b><strong>HISTORICAL</strong><small>Performance</small></div>
    <div class="topic" style="left:186px;top:52px"><b style="background:var(--yellow)"></b><strong>FINANCIAL</strong><small>Review</small></div>
    <div class="qa" style="left:140px">Q&amp;A</div>
    <div class="foot"><div class="by">by</div><div class="maker">kelvanoro+</div><div class="btn"></div></div>
  </section>

  <section class="slide c2 r3">
    <div class="brand lg" style="left:82px;top:14px"><i></i>Velmora</div>
    <div class="band" style="top:53px;height:56px;background:#353f52"></div>
    <div class="agenda-word">AGENDA</div>
    <div class="agenda-note">A short outline of the topics in this half year review.</div>
    <div class="divider"></div>
    <div class="topic" style="left:86px;top:52px"><b style="background:var(--orange)"></b><strong>BALANCE</strong><small>SHEET</small></div>
    <div class="topic" style="left:136px;top:52px"><b style="background:var(--silver)"></b><strong>INCOME</strong><small>STATEMENT</small></div>
    <div class="topic" style="left:186px;top:52px"><b style="background:var(--yellow)"></b><strong>FINANCIAL</strong><small>HIGHLIGHTS</small></div>
    <div class="qa" style="left:140px">Q&amp;A</div>
    <div class="foot"><div class="by">by</div><div class="maker">kelvanoro+</div><div class="btn"></div></div>
  </section>

  <section class="slide c3 r3" style="background:linear-gradient(140deg,#3272ba,#2a67ad 60%,#2d6ab1)">
    <div style="position:absolute;right:2px;top:2px;width:36px;height:15px;background:#fff"></div>
    <div class="brand sm" style="right:5px;top:6px"><i></i>Velmora</div>
    <div style="position:absolute;right:34px;top:62px;text-align:center;color:#fff;font-weight:700;font-size:14px;line-height:1.25">BALANCE<br>SHEET</div>
    <div style="position:absolute;right:2px;bottom:1px;width:50px;height:9px;background:#fff"></div>
    <div class="maker" style="right:5px;bottom:2px;font-size:5.5px">kelvanoro+</div>
  </section>

  <section class="slide c1 r4">
    <div class="head"><h3>Assets</h3><small>ABC Company Balance Sheet as of June 30, 2017</small><div class="brand sm"><i></i>Velmora</div></div>
    <div class="block b1" style="top:37px;height:75px"></div>
    <div class="block b2" style="top:37px;height:75px"></div>
    <div class="block b3" style="top:37px;height:75px"></div>
    <div class="colhead" style="left:84px;top:33px">30-June-2017</div>
    <div class="colhead" style="left:142px;top:33px">30-May-2017</div>
    <div class="colhead" style="left:200px;top:33px">30-Apr-2017</div>
    <div class="label sec" style="top:39px">Fixed Assets</div>
    <div class="label" style="top:47px">Cars</div>
    <div class="label" style="top:53px">Machines</div>
    <div class="label" style="top:59px">Total Assets</div>
    <div class="label" style="top:65px">Accum. Depreciation</div>
    <div class="cell" style="left:78px;top:47px">16,800</div><div class="cell" style="left:135px;top:47px">16,650</div><div class="cell" style="left:192px;top:47px">16,500</div>
    <div class="cell" style="left:78px;top:53px">2,200</div><div class="cell" style="left:135px;top:53px">2,200</div><div class="cell" style="left:192px;top:53px">2,200</div>
    <div class="cell" style="left:78px;top:59px">19,000</div><div class="cell" style="left:135px;top:59px">18,850</div><div class="cell" style="left:192px;top:59px">18,700</div>
    <div class="cell" style="left:78px;top:65px">(13,490)</div><div class="cell" style="left:135px;top:65px">(13,109)</div><div class="cell" style="left:192px;top:65px">(12,720)</div>
    <div class="navband" style="top:76px"><span style="left:10px">Net Fixed Assets</span><span style="left:78px">5,510</span><span style="left:135px">5,741</span><span style="left:192px">5,980</span></div>
    <div class="foot"><div class="by">by</div><div class="maker">kelvanoro+</div><div class="btn"></div></div>
  </section>

  <section class="slide c2 r4">
    <div class="head"><h3>Fixed Assets Graphical View</h3><small>ABC Company</small><div class="brand sm"><i></i>Velmora</div></div>
    <div class="chart-area">
      <svg width="118" height="88" viewBox="0 0 118 88" font-family="Open Sans, sans-serif">
        <g fill="#dbe6f3" font-size="3">
          <text x="0" y="12">60%</text><text x="0" y="22">50%</text><text x="0" y="32">40%</text><text x="0" y="42">30%</text><text x="0" y="52">20%</text><text x="0" y="62">10%</text><text x="0" y="72">0%</text>
        </g>
        <g fill="#fff"><rect x="30" y="28" width="9" height="42"/><rect x="58" y="21" width="9" height="49"/><rect x="86" y="25" width="9" height="45"/></g>
        <g fill="#fff" font-size="3.4" text-anchor="middle"><text x="34" y="26">42%</text><text x="62" y="19">49%</text><text x="90" y="23">45%</text>
        <text x="34" y="76" font-size="2.6">30-June-2017</text><text x="62" y="76" font-size="2.6">30-May-2017</text><text x="90" y="76" font-size="2.6">30-Apr-2017</text>
        <text x="62" y="82" font-size="2.6">■ Net Fixed Assets</text></g>
      </svg>
      <div class="quarter">QUARTER - I</div>
      <div class="val-col"><em>Value</em></div><div class="pct-col"><em>%</em></div>
      <div class="row" style="top:38px"><span class="d">30-June-2017</span><span class="v">5,510</span><span class="p">42%</span></div>
      <div class="row" style="top:60px"><span class="d">30-May-2017</span><span class="v">5,741</span><span class="p">49%</span></div>
      <div class="row" style="top:84px"><span class="d">30-Apr-2017</span><span class="v">5,980</span><span class="p">45%</span></div>
    </div>
    <div class="foot"><div class="by">by</div><div class="maker">kelvanoro+</div><div class="btn"></div></div>
  </section>

  <section class="slide c3 r4">
    <div class="head"><h3>Assets</h3><small>ABC Company Balance Sheet as of June 30, 2017</small><div class="brand sm"><i></i>Velmora</div></div>
    <div class="block b1" style="top:34px;height:67px"></div>
    <div class="block b2" style="top:34px;height:67px"></div>
    <div class="block b3" style="top:34px;height:67px"></div>
    <div class="colhead" style="left:84px;top:30px">30-June-2017</div>
    <div class="colhead" style="left:142px;top:30px">30-May-2017</div>
    <div class="colhead" style="left:200px;top:30px">30-Apr-2017</div>
    <div class="label sec" style="top:35px">Current Assets</div>
    <div class="label" style="top:43px">Accounts Receivable</div>
    <div class="label" style="top:50px">Inventory</div>
    <div class="label" style="top:57px">Staff loan</div>
    <div class="label sec" style="top:64px">Bank</div>
    <div class="label" style="top:72px">Cash on hand</div>
    <div class="label" style="top:79px">Bank Account</div>
    <div class="label" style="top:86px">E-wallet</div>
    <div class="label" style="top:93px">Total Bank</div>
    <div class="cell" style="left:78px;top:43px">334</div><div class="cell" style="left:135px;top:43px">324</div><div class="cell" style="left:192px;top:43px">314</div>
    <div class="cell" style="left:78px;top:50px">1,472</div><div class="cell" style="left:135px;top:50px">1,472</div><div class="cell" style="left:192px;top:50px">1,472</div>
    <div class="cell" style="left:78px;top:72px">1,327</div><div class="cell" style="left:135px;top:72px">1,327</div><div class="cell" style="left:192px;top:72px">1,327</div>
    <div class="cell" style="left:78px;top:79px">2,136</div><div class="cell" style="left:135px;top:79px">2,136</div><div class="cell" style="left:192px;top:79px">2,136</div>
    <div class="cell" style="left:78px;top:93px">5,790</div><div class="cell" style="left:135px;top:93px">5,790</div><div class="cell" style="left:192px;top:93px">5,790</div>
    <div class="navband" style="top:102px"><span style="left:10px">Total Current Assets</span><span style="left:78px">7,627</span><span style="left:135px">5,915</span><span style="left:192px">7,420</span></div>
    <div class="totals" style="top:111px"><span style="left:10px">Total Assets</span><span style="left:78px">13,137</span><span style="left:102px">100%</span><span style="left:135px">11,655</span><span style="left:159px">100%</span><span style="left:192px">13,400</span><span style="left:216px">100%</span></div>
    <div class="foot"><div class="by">by</div><div class="maker">kelvanoro+</div><div class="btn"></div></div>
  </section>

  <section class="slide c1 r5">
    <div class="head"><h3>Total Current Assets Graphical View</h3><small>ABC Company</small><div class="brand sm"><i></i>Velmora</div></div>
    <div class="chart-area">
      <svg width="118" height="88" viewBox="0 0 118 88" font-family="Open Sans, sans-serif">
        <g fill="#dbe6f3" font-size="3">
          <text x="0" y="12">60%</text><text x="0" y="22">50%</text><text x="0" y="32">40%</text><text x="0" y="42">30%</text><text x="0" y="52">20%</text><text x="0" y="62">10%</text><text x="0" y="72">0%</text>
        </g>
        <g fill="#fff"><rect x="30" y="12" width="9" height="58"/><rect x="58" y="19" width="9" height="51"/><rect x="86" y="15" width="9" height="55"/></g>
        <g fill="#fff" font-size="3.4" text-anchor="middle"><text x="34" y="10">58%</text><text x="62" y="17">51%</text><text x="90" y="13">55%</text>
        <text x="34" y="76" font-size="2.6">30-June-2017</text><text x="62" y="76" font-size="2.6">30-May-2017</text><text x="90" y="76" font-size="2.6">30-Apr-2017</text>
        <text x="62" y="82" font-size="2.6">■ Total Current Assets</text></g>
      </svg>
      <div class="quarter">QUARTER - I</div>
      <div class="val-col"><em>Value</em></div><div class="pct-col"><em>%</em></div>
      <div class="row" style="top:38px"><span class="d">30-June-2017</span><span class="v">7,627</span><span class="p">58%</span></div>
      <div class="row" style="top:60px"><span class="d">30-May-2017</span><span class="v">5,915</span><span class="p">51%</span></div>
      <div class="row" style="top:84px"><span class="d">30-Apr-2017</span><span class="v">7,420</span><span class="p">55%</span></div>
    </div>
    <div class="foot"><div class="by">by</div><div class="maker">kelvanoro+</div><div class="btn"></div></div>
  </section>

  <section class="slide c2 r5">
    <div class="head"><h3>Liabilities &amp; Equity</h3><small>ABC Company Balance Sheet as of June 30, 2017</small><div class="brand sm"><i></i>Velmora</div></div>
    <div class="block b1" style="top:38px;height:74px"></div>
    <div class="block b2" style="top:38px;height:74px"></div>
    <div class="block b3" style="top:38px;height:74px"></div>
    <div class="colhead" style="left:84px;top:34px">30-June-2017</div>
    <div class="colhead" style="left:142px;top:34px">30-May-2017</div>
    <div class="colhead" style="left:200px;top:34px">30-Apr-2017</div>
    <div class="label sec" style="top:40px">Liabilities</div>
    <div class="label" style="top:50px">Accounts Payable</div>
    <div class="label" style="top:56px">Accrued Expenses</div>
    <div class="label" style="top:62px">Loan</div>
    <div class="cell" style="left:78px;top:50px">285</div><div class="cell" style="left:135px;top:50px">285</div><div class="cell" style="left:192px;top:50px">285</div>
    <div class="cell" style="left:78px;top:56px">1,180</div><div class="cell" style="left:135px;top:56px">1,180</div><div class="cell" style="left:192px;top:56px">1,180</div>
    <div class="cell" style="left:78px;top:62px">1,608</div><div class="cell" style="left:135px;top:62px">1,608</div><div class="cell" style="left:192px;top:62px">1,608</div>
    <div class="navband" style="top:77px"><span style="left:10px">Total Liabilities</span><span style="left:78px">3,653</span><span style="left:135px">3,653</span><span style="left:192px">3,653</span></div>
    <div class="foot"><div class="by">by</div><div class="maker">kelvanoro+</div><div class="btn"></div></div>
  </section>

  <section class="slide c3 r5">
    <div class="head"><h3>Total Liabilities Graphical View</h3><small>ABC Company</small><div class="brand sm"><i></i>Velmora</div></div>
    <div class="chart-area">
      <svg width="118" height="88" viewBox="0 0 118 88" font-family="Open Sans, sans-serif">
        <g fill="#dbe6f3" font-size="3">
          <text x="0" y="12">60%</text><text x="0" y="22">50%</text><text x="0" y="32">40%</text><text x="0" y="42">30%</text><text x="0" y="52">20%</text><text x="0" y="62">10%</text><text x="0" y="72">0%</text>
        </g>
        <g fill="#fff"><rect x="30" y="42" width="9" height="28"/><rect x="58" y="50" width="9" height="20"/><rect x="86" y="52" width="9" height="18"/></g>
        <g fill="#fff" font-size="3.4" text-anchor="middle"><text x="34" y="40">28%</text><text x="62" y="48">20%</text><text x="90" y="50">18%</text>
        <text x="34" y="76" font-size="2.6">30-June-2017</text><text x="62" y="76" font-size="2.6">30-May-2017</text><text x="90" y="76" font-size="2.6">30-Apr-2017</text>
        <text x="62" y="82" font-size="2.6">■ Total Liabilities</text></g>
      </svg>
      <div class="quarter">QUARTER - I</div>
      <div class="val-col"><em>Value</em></div><div class="pct-col"><em>%</em></div>
      <div class="row" style="top:38px"><span class="d">30-June-2017</span><span class="v">5,510</span><span class="p">28%</span></div>
      <div class="row" style="top:60px"><span class="d">30-May-2017</span><span class="v">5,741</span><span class="p">20%</span></div>
      <div class="row" style="top:84px"><span class="d">30-Apr-2017</span><span class="v">5,980</span><span class="p">18%</span></div>
    </div>
    <div class="foot"><div class="by">by</div><div class="maker">kelvanoro+</div><div class="btn"></div></div>
  </section>

  <section class="slide c1 r6">
    <div class="head"><h3>Liabilities &amp; Equity</h3><small>ABC Company Balance Sheet as of June 30, 2017</small><div class="brand sm"><i></i>Velmora</div></div>
    <div class="block b1" style="top:36px;height:66px"></div>
    <div class="block b2" style="top:36px;height:66px"></div>
    <div class="block b3" style="top:36px;height:66px"></div>
    <div class="colhead" style="left:84px;top:32px">30-June-2017</div>
    <div class="colhead" style="left:142px;top:32px">30-May-2017</div>
    <div class="colhead" style="left:200px;top:32px">30-Apr-2017</div>
    <div class="label sec" style="top:37px">Partner's Equity</div>
    <div class="label" style="top:44px">Capital</div>
    <div class="label" style="top:50px">Current Accounts</div>
    <div class="label" style="top:56px">C/A Partner 1</div>
    <div class="label" style="top:62px">C/A Partner 2</div>
    <div class="label" style="top:68px">C/A Partner 3</div>
    <div class="label" style="top:82px">Retained Earnings</div>
    <div class="label" style="top:88px">Current Earnings</div>
    <div class="cell" style="left:78px;top:44px">20,000</div><div class="cell" style="left:135px;top:44px">20,000</div><div class="cell" style="left:192px;top:44px">20,000</div>
    <div class="cell" style="left:78px;top:56px">400</div><div class="cell" style="left:135px;top:56px">400</div><div class="cell" style="left:192px;top:56px">400</div>
    <div class="cell" style="left:78px;top:62px">(1,800)</div><div class="cell" style="left:135px;top:62px">(1,800)</div><div class="cell" style="left:192px;top:62px">(1,800)</div>
    <div class="cell" style="left:78px;top:82px">(12,651)</div><div class="cell" style="left:135px;top:82px">(13,051)</div><div class="cell" style="left:192px;top:82px">(12,051)</div>
    <div style="position:absolute;left:0;top:74px;width:238px;height:5px;background:rgba(31,45,69,.25)"></div>
    <div class="navband" style="top:104px"><span style="left:10px">Total Partner's Equity</span><span style="left:78px">9,484</span><span style="left:135px">9,305</span><span style="left:192px">10,931</span></div>
    <div class="totals" style="top:112px"><span style="left:10px">Total Liabilities &amp; Equity</span><span style="left:78px">13,137</span><span style="left:102px">100%</span><span style="left:135px">11,655</span><span style="left:159px">100%</span><span style="left:192px">13,400</span><span style="left:216px">100%</span></div>
    <div class="foot"><div class="by">by</div><div class="maker">kelvanoro+</div><div class="btn"></div></div>
  </section>

  <section class="slide c2 r6">
    <div class="head"><h3>Total Partner's Equity Graphical View</h3><small>ABC Company</small><div class="brand sm"><i></i>Velmora</div></div>
    <div class="chart-area">
      <svg width="118" height="88" viewBox="0 0 118 88" font-family="Open Sans, sans-serif">
        <g fill="#dbe6f3" font-size="3">
          <text x="0" y="12">90%</text><text x="0" y="22">75%</text><text x="0" y="32">60%</text><text x="0" y="42">45%</text><text x="0" y="52">30%</text><text x="0" y="62">15%</text><text x="0" y="72">0%</text>
        </g>
        <g fill="#fff"><rect x="30" y="22" width="9" height="48"/><rect x="58" y="17" width="9" height="53"/><rect x="86" y="15" width="9" height="55"/></g>
        <g fill="#fff" font-size="3.4" text-anchor="middle"><text x="34" y="20">72%</text><text x="62" y="15">80%</text><text x="90" y="13">82%</text>
        <text x="34" y="76" font-size="2.6">30-June-2017</text><text x="62" y="76" font-size="2.6">30-May-2017</text><text x="90" y="76" font-size="2.6">30-Apr-2017</text>
        <text x="62" y="82" font-size="2.6">■ Total Partner's Equity</text></g>
      </svg>
      <div class="quarter">QUARTER - I</div>
      <div class="val-col"><em>Value</em></div><div class="pct-col"><em>%</em></div>
      <div class="row" style="top:38px"><span class="d">30-June-2017</span><span class="v">9,484</span><span class="p">72%</span></div>
      <div class="row" style="top:60px"><span class="d">30-May-2017</span><span class="v">9,305</span><span class="p">80%</span></div>
      <div class="row" style="top:84px"><span class="d">30-Apr-2017</span><span class="v">10,931</span><span class="p">82%</span></div>
    </div>
    <div class="foot"><div class="by">by</div><div class="maker">kelvanoro+</div><div class="btn"></div></div>
  </section>

  <section class="slide c3 r6">
    <div class="head"><h3>Total Liabilities &amp; Equity</h3><small>ABC Company</small><div class="brand sm"><i></i>Velmora</div></div>
    <div class="chart-area">
      <svg width="118" height="88" viewBox="0 0 118 88" font-family="Open Sans, sans-serif">
        <g fill="#dbe6f3" font-size="3">
          <text x="0" y="12">14000</text><text x="0" y="22">12000</text><text x="0" y="32">10000</text><text x="0" y="42">8000</text><text x="0" y="52">6000</text><text x="0" y="62">4000</text><text x="0" y="72">2000</text>
        </g>
        <g fill="#fff"><rect x="30" y="14" width="9" height="56"/><rect x="58" y="20" width="9" height="50"/><rect x="86" y="13" width="9" height="57"/></g>
        <g fill="#fff" font-size="3.2" text-anchor="middle"><text x="34" y="12">13137</text><text x="62" y="18">11655</text><text x="90" y="11">13400</text>
        <text x="34" y="76" font-size="2.6">30-June-2017</text><text x="62" y="76" font-size="2.6">30-May-2017</text><text x="90" y="76" font-size="2.6">30-Apr-2017</text>
        <text x="62" y="82" font-size="2.6">■ Total Liabilities &amp; Equity</text></g>
      </svg>
      <div class="quarter">QUARTER - I</div>
      <div class="val-col"><em>Value</em></div><div class="pct-col"><em>%</em></div>
      <div class="row" style="top:38px"><span class="d">30-June-2017</span><span class="v">13,137</span><span class="p">100%</span></div>
      <div class="row" style="top:60px"><span class="d">30-May-2017</span><span class="v">11,655</span><span class="p">100%</span></div>
      <div class="row" style="top:84px"><span class="d">30-Apr-2017</span><span class="v">13,400</span><span class="p">100%</span></div>
    </div>
    <div class="foot"><div class="by">by</div><div class="maker">kelvanoro+</div><div class="btn"></div></div>
  </section>
</div>
</body>
</html>
```